Brolvane Co.,Ltd. need business card

Brolvane Company Limited is a facility management company. We provides a total solution services from administration, energy saving, security, safety, food catering to companies.

The logo should be in elegant style with innovative that suited to the upper market
Please see the logo image in the attached file. You can use this Red or Blue or Green checkerboard (color and font should be similar to logo) as the main part of business card (can be an entire of one side of business card) . In another side of card should contain contact details of personnel - here below demo information

Kanyarat Thoengsai
Chief Executive Officer

No.73, Soi 5, Ruam Wongsa Road
Nong Khaem, Bangkok,
10520, Thailand

Tel + 66841537296
Mobile + 66841537296
E-mail: Kanyarat.Thoengsai@brolvane-example.co.th

Target Market(s)

Factory, Hotel and Hospital

Industry/Entity Type

Business

Contact Information for Business Card

Kanyarat Thoengsai
Chief Executive Officer

Nong Khaem, Bangkok,
10520, Thailand

Tel + 66841537296
Mobile + 66841537296

We will change details with the winner designer

Font styles to use
Sans Serif

Requirements
Must have
• In style of red checkerboard and white color

```html
<!DOCTYPE html>
<html lang="en">
<head>
<meta charset="utf-8">
<title>Brolvane Co.,Ltd. – Business Card</title>
<link rel="stylesheet" href="https://fonts.googleapis.com/css2?family=Open+Sans:wght@400;700&display=swap">
<style>
  :root {
    --canvas-bg: #3a3a3a;
    --front-red: #4a1014;
    --front-red-deep: #3a0b0e;
    --back-black: #050505;
    --ink-white: #ffffff;
    --ink-soft: #d8d8d8;
    --divider: #8a8a8a;
    --radius: 20px;
  }
  * { box-sizing: border-box; margin: 0; padding: 0; }
  html, body {
    width: 1200px; height: 900px; overflow: hidden;
    background: var(--canvas-bg);
    font-family: "Open Sans", Arial, sans-serif;
  }
  .canvas {
    width: 1200px; height: 900px;
    display: flex; flex-direction: column;
    align-items: center; justify-content: center;
    gap: 56px;
  }
  .card {
    width: 600px; height: 343px;
    border-radius: var(--radius);
    position: relative; overflow: hidden;
    box-shadow: 0 14px 30px rgba(0,0,0,0.45);
  }
  .card-front {
    background: radial-gradient(ellipse at 50% 45%, var(--front-red) 0%, var(--front-red-deep) 100%);
    display: flex; align-items: center; justify-content: center;
  }
  .brand-name {
    color: var(--ink-white);
    font-family: "Open Sans", Arial, sans-serif;
    font-weight: 400;
    letter-spacing: 0.22em;
    line-height: 1;
  }
  .card-front .brand-name { font-size: 52px; position: relative; }
  .card-back {
    background: var(--back-black);
    display: flex; align-items: center;
  }
  .card-back .brand-name {
    font-size: 34px;
    width: 300px;
    text-align: center;
    padding-left: 18px;
  }
  .divider {
    width: 1px; height: 190px;
    background: linear-gradient(to bottom, transparent, var(--divider) 15%, var(--divider) 85%, transparent);
  }
  .contact {
    padding-left: 14px;
    color: var(--ink-soft);
    font-size: 12.5px;
    line-height: 1.38;
  }
  .contact .person { color: var(--ink-white); font-weight: 700; font-size: 17px; line-height: 1.2; }
  .contact .role { margin-bottom: 12px; }
  .contact .address { margin-bottom: 6px; }
  .contact .line { display: flex; align-items: center; gap: 7px; }
  .contact .line svg { width: 10px; height: 10px; flex: none; }
</style>
</head>
<body>
<main class="canvas">
  <section class="card card-front" role="img" aria-label="Deep red checkerboard background with the Brolvane name">
    <span class="brand-name">BROLVANE</span>
  </section>

  <section class="card card-back">
    <span class="brand-name">BROLVANE</span>
    <span class="divider"></span>
    <div class="contact">
      <p class="person">Kanyarat Thoengsai</p>
      <p class="role">Chief Executive Officer</p>
      <p class="address">No.73, Soi 5, Ruam Wongsa Road<br>Nong Khaem, Bangkok,<br>10520, Thailand</p>
      <p class="line">
        <svg viewBox="0 0 10 10" aria-hidden="true"><path d="M2 1 L3.6 1 L4.2 3 L3.1 3.8 Q4 5.9 6.2 6.9 L7 5.8 L9 6.4 L9 8 Q8.5 9 7.5 9 Q1 8 1 2 Q1 1 2 1Z" fill="#d8d8d8"/></svg>
        + 668 4153 7296
      </p>
      <p class="line">
        <svg viewBox="0 0 10 10" aria-hidden="true"><rect x="2.5" y="0.5" width="5" height="9" rx="1" fill="none" stroke="#d8d8d8"/><circle cx="5" cy="8" r="0.6" fill="#d8d8d8"/></svg>
        + 668 4153 7296
      </p>
      <p class="line">
        <svg viewBox="0 0 10 10" aria-hidden="true"><rect x="0.5" y="2" width="9" height="6" fill="none" stroke="#d8d8d8"/><path d="M0.5 2 L5 5.5 L9.5 2" fill="none" stroke="#d8d8d8"/></svg>
        Kanyarat.Thoengsai@brolvane-example.co.th
      </p>
    </div>
  </section>
</main>
</body>
</html>
```